PDF flyer to go out to Medical Providers: 2 sided A4

We need to design a 2 sided A4 pamphlet which we can email out to prospective clients.

We are a recruitment company and wish to provide staff to healthcare providers

We are a medical recruitment agency. We need to be able to write approximately 600 words, split up into 4 sub headings. Text has been provided on the uploaded word document. THIS TEXT IS DRAFT ONLY AND WILL CHANGE.

We need to look professional & efficient

Target Market(s)

Hospitals, srugeries

Industry/Entity Type

Medical

Requirements
Must have
• Room for 600 words, which will b echanged once the layout is confirmed
Nice to have
• Have it in Word form so we can use it for subsequent mail outs.

```html
<!DOCTYPE html>
<html lang="en">
<head>
<meta charset="utf-8">
<title>Carewell Staffing – Specialist Nursing Flyer</title>
<link href="https://fonts.googleapis.com/css2?family=Oswald:wght@500;600&family=Open+Sans:wght@400;600;700&display=swap" rel="stylesheet">
<style>
  :root{
    --teal:#1bb3b8;
    --teal-light:#3cc9c9;
    --teal-dark:#0e7f86;
    --navy-teal:#0b5d66;
    --grey-text:#5b6870;
    --body-text:#3b4a52;
    --photo-a:#e9eef0;
    --photo-b:#c9d6dc;
    --white:#ffffff;
  }
  *{box-sizing:border-box;margin:0;padding:0}
  html,body{width:807px;height:1200px;overflow:hidden;background:#f4f6f7}
  body{font-family:"Open Sans",Arial,sans-serif;color:var(--body-text)}
  .flyer{position:relative;width:807px;height:1200px;background:var(--white);overflow:hidden}

  .top-band{position:absolute;left:0;top:0;width:807px;height:110px}
  .top-band .headline{position:absolute;left:0;top:30px;width:100%;text-align:center;
    font-family:"Open Sans",Arial,sans-serif;font-weight:700;font-size:26px;color:var(--white);letter-spacing:.5px}

  .hero-photo{position:absolute;left:0;top:90px;width:807px;height:430px;
    background:linear-gradient(135deg,var(--photo-a) 0%,var(--photo-b) 60%,#b6c7cf 100%)}

  .brand{position:absolute;left:36px;top:170px;display:flex;align-items:center;gap:10px}
  .brand .dot{width:26px;height:26px;border-radius:50%;background:var(--teal)}
  .brand .name{font-family:"Open Sans",Arial,sans-serif;font-weight:600;font-size:22px;color:var(--teal-dark)}

  .waves{position:absolute;left:0;top:420px;width:807px;height:140px}

  .intro{position:absolute;left:34px;top:548px;width:380px}
  .intro h1{font-family:"Oswald",Arial,sans-serif;font-weight:600;font-size:42px;line-height:1.05;color:var(--teal);letter-spacing:.5px;white-space:nowrap}
  .intro .sub{font-family:"Oswald",Arial,sans-serif;font-weight:500;font-size:22px;line-height:1.2;color:var(--grey-text);margin-top:4px;letter-spacing:.5px;white-space:nowrap}

  .section-bar{position:absolute;left:0;width:400px;height:32px;background:linear-gradient(90deg,var(--teal-dark),var(--teal));
    border-radius:0 16px 16px 0;color:var(--white);font-family:"Oswald",Arial,sans-serif;font-weight:500;font-size:19px;
    padding:3px 34px;letter-spacing:.5px}
  .section-text{position:absolute;left:34px;width:366px;font-size:14.5px;line-height:1.45;color:var(--body-text)}
  .about-bar{top:664px}
  .about-text{top:706px}
  .philosophy-bar{top:830px}
  .philosophy-text{top:872px}

  .specialisms{position:absolute;left:420px;top:520px;width:387px;height:600px;
    background:linear-gradient(180deg,var(--teal) 0%,var(--teal-light) 100%);border-radius:24px 0 0 0;padding:26px 22px 0 22px}
  .specialisms .pill{display:block;width:330px;margin:0 auto;background:var(--navy-teal);color:var(--white);border-radius:24px;
    text-align:center;font-family:"Oswald",Arial,sans-serif;font-weight:600;font-size:26px;padding:4px 0;letter-spacing:.5px}
  .specialisms .lead{margin-top:16px;text-align:center;font-size:14px;line-height:1.45;color:var(--white)}
  .spec-list{list-style:none;margin-top:22px}
  .spec-list li{display:flex;align-items:flex-start;gap:10px;color:var(--white);font-size:14.5px;font-weight:600;line-height:1.35;margin-bottom:17px}
  .spec-list svg{flex:none;margin-top:2px}

  .contact-bar{position:absolute;left:0;top:1120px;width:807px;height:80px;background:var(--navy-teal);
    display:flex;align-items:center;justify-content:space-around;padding:0 20px}
  .contact-item{display:flex;align-items:center;gap:10px;color:var(--white);font-size:19px;font-weight:600}
</style>
</head>
<body>
<div class="flyer">

  <div class="hero-photo" role="img" aria-label="Photo of a nurse and doctor caring for a smiling elderly male patient"></div>

  <svg class="top-band" viewBox="0 0 807 110" aria-hidden="true">
    <defs>
      <linearGradient id="bandGrad" x1="0" x2="1" y1="0" y2="0">
        <stop offset="0" stop-color="#0e7f86"/>
        <stop offset=".5" stop-color="#1bb3b8"/>
        <stop offset="1" stop-color="#0e7f86"/>
      </linearGradient>
    </defs>
    <path d="M0 0H807V82Q404 118 0 82Z" fill="url(#bandGrad)"/>
    <path d="M0 88Q404 124 807 88" stroke="#7fdcdc" stroke-width="3" fill="none"/>
  </svg>
  <div class="top-band"><div class="headline">SPECIAL CARE OUR CONSULTANTS ARE AVAILABLE</div></div>

  <div class="brand"><span class="dot"></span><span class="name">Carewell Staffing</span></div>

  <svg class="waves" viewBox="0 0 807 140" aria-hidden="true">
    <path d="M0 70Q300 20 807 40V140H0Z" fill="#ffffff"/>
    <path d="M0 62Q300 10 807 30" stroke="#1bb3b8" stroke-width="8" fill="none"/>
    <path d="M0 80Q320 30 807 52" stroke="#7fdcdc" stroke-width="3" fill="none"/>
  </svg>

  <div class="intro">
    <h1>A SPECIALIST TEAM</h1>
    <div class="sub">DEDICATED TO SPECIAL CARE</div>
  </div>

  <div class="section-bar about-bar">ABOUT US</div>
  <p class="section-text about-text">Meridian Nursing was established with a sole focus to provide nationwide recruitment solutions for specialist sector nursing requirements. We have over 30 years industry experience and successfully deliver nursing solutions to client requirements.</p>

  <div class="section-bar philosophy-bar">OUR PHILOSOPHY</div>
  <p class="section-text philosophy-text">Our philosophy is to be masters in our supply of specialist staff rather than diluting our service by over generalising. This ethos was naturally birthed from supplying to all types of healthcare establishments and identifying a trend whereby agencies could fill easier bookings – still leaving the client with those important and hard to fill requirements and ultimately falling short of providing a full service.</p>

  <section class="specialisms">
    <span class="pill">OUR SPECIALISMS</span>
    <p class="lead">Our consultants provide a professional and effective service in the supply of the following speciality nurses:</p>
    <ul class="spec-list">
      <li><svg width="16" height="16" viewBox="0 0 16 16"><circle cx="8" cy="8" r="8" fill="#fff"/><path d="M6 4l4 4-4 4" stroke="#0e7f86" stroke-width="2" fill="none"/></svg>Theatre (Scrub, Anaesthetics, Recovery) and ODP's</li>
      <li><svg width="16" height="16" viewBox="0 0 16 16"><circle cx="8" cy="8" r="8" fill="#fff"/><path d="M6 4l4 4-4 4" stroke="#0e7f86" stroke-width="2" fill="none"/></svg>A&amp;E Nurses</li>
      <li><svg width="16" height="16" viewBox="0 0 16 16"><circle cx="8" cy="8" r="8" fill="#fff"/><path d="M6 4l4 4-4 4" stroke="#0e7f86" stroke-width="2" fill="none"/></svg>ITU / HDU / CCU Nurses</li>
      <li><svg width="16" height="16" viewBox="0 0 16 16"><circle cx="8" cy="8" r="8" fill="#fff"/><path d="M6 4l4 4-4 4" stroke="#0e7f86" stroke-width="2" fill="none"/></svg>Paediatric Nurses (General Paeds, PICU &amp; NICU)</li>
      <li><svg width="16" height="16" viewBox="0 0 16 16"><circle cx="8" cy="8" r="8" fill="#fff"/><path d="M6 4l4 4-4 4" stroke="#0e7f86" stroke-width="2" fill="none"/></svg>RMN &amp; CPN's</li>
      <li><svg width="16" height="16" viewBox="0 0 16 16"><circle cx="8" cy="8" r="8" fill="#fff"/><path d="M6 4l4 4-4 4" stroke="#0e7f86" stroke-width="2" fill="none"/></svg>Oncology Nurses</li>
      <li><svg width="16" height="16" viewBox="0 0 16 16"><circle cx="8" cy="8" r="8" fill="#fff"/><path d="M6 4l4 4-4 4" stroke="#0e7f86" stroke-width="2" fill="none"/></svg>Community / District Nurses</li>
      <li><svg width="16" height="16" viewBox="0 0 16 16"><circle cx="8" cy="8" r="8" fill="#fff"/><path d="M6 4l4 4-4 4" stroke="#0e7f86" stroke-width="2" fill="none"/></svg>Midwives</li>
    </ul>
  </section>

  <footer class="contact-bar">
    <div class="contact-item">
      <svg width="28" height="28" viewBox="0 0 28 28"><circle cx="14" cy="14" r="14" fill="#1bb3b8"/><path d="M10 7l3 3-2 2q1 3 5 5l2-2 3 3-2 3q-6 0-11-5t-4-11z" fill="#fff"/></svg>
      555-014-2290
    </div>
    <div class="contact-item">
      <svg width="28" height="28" viewBox="0 0 28 28"><circle cx="14" cy="14" r="14" fill="#1bb3b8"/><rect x="7" y="9" width="14" height="10" fill="#fff"/><path d="M7 9l7 6 7-6" stroke="#1bb3b8" stroke-width="1.5" fill="none"/></svg>
      info@carewellstaff.com
    </div>
    <div class="contact-item">
      <svg width="28" height="28" viewBox="0 0 28 28"><circle cx="14" cy="14" r="14" fill="#1bb3b8"/><circle cx="14" cy="14" r="7" stroke="#fff" stroke-width="1.6" fill="none"/><path d="M7 14h14M14 7q-4 7 0 14M14 7q4 7 0 14" stroke="#fff" stroke-width="1.4" fill="none"/></svg>
      www.carewellstaff.com
    </div>
  </footer>
</div>
</body>
</html>
```